We Are Corvale Marketing Collateral

We Are Corvale has undergone a rebrand with new logo, website, and intranet design builds. The business is now looking to update its marketing collateral with the new logo design and colour palette. Deliverables include PowerPoint template, Report template, Letterhead, and Email signature. Refer attached design brief for more information. Also attached are the logo and brand document.
Target Market(s)
Executive & Board of SME impact organisations.
Industry/Entity Type
We serve small to medium organisations who are delivering impact, not-for-profits, social enterprises and purpose driven organisations.
Font styles to use
Other font styles liked:
- Roca Two Thin, Rubik Regular
Look and feel
Each slider illustrates characteristics of the customer's brand and the style your logo design should communicate.

```html
<!DOCTYPE html>
<html lang="en">
<head>
<meta charset="utf-8">
<title>We Are Corvale – Letterhead</title>
<link rel="stylesheet" href="https://fonts.googleapis.com/css2?family=Open+Sans:wght@300;400&family=Lora:wght@400&family=Pinyon+Script&display=swap">
<style>
  :root {
    --backdrop: #e4e4e4;
    --paper: #f1f1f1;
    --ink: #2b2b2b;
    --brand-dark: #174745;
    --band-teal-dark: #14443f;
    --band-orange: #e5803a;
    --band-teal: #2b8a97;
    --band-red: #e05555;
    --band-plum: #ad3e68;
    --band-green: #3f9e6a;
    --accent-orange: #e07628;
    --pattern-grey: #dcdcdc;
  }
  * { margin: 0; padding: 0; box-sizing: border-box; }
  html, body { width: 1200px; height: 1200px; overflow: hidden; }
  body { background: var(--backdrop); position: relative; }

  .letterhead {
    position: absolute; left: 204px; top: 40px;
    width: 792px; height: 1120px;
    background: var(--paper);
    box-shadow: 0 2px 8px rgba(0,0,0,0.12);
    overflow: hidden;
  }
  .color-spine {
    position: absolute; left: 0; top: 0; width: 15px; height: 100%;
    display: flex; flex-direction: column;
  }
  .color-spine span { flex: 1; }
  .color-spine .s1 { background: var(--band-teal-dark); }
  .color-spine .s2 { background: var(--band-orange); }
  .color-spine .s3 { background: var(--band-teal); }
  .color-spine .s4 { background: var(--band-red); }
  .color-spine .s5 { background: var(--band-plum); }
  .color-spine .s6 { background: var(--band-green); }

  .brand-decoration {
    position: absolute; right: 0; top: 0; width: 275px; height: 272px;
    background: radial-gradient(circle at 78% 38%, var(--pattern-grey) 0%, rgba(220,220,220,0.55) 45%, rgba(241,241,241,0) 72%);
  }

  .brand-lockup {
    position: absolute; left: 80px; top: 40px;
    display: flex; align-items: center; gap: 18px; height: 78px;
  }
  .brand-mark { width: 74px; height: 74px; border-radius: 50%; background: var(--band-orange); }
  .brand-name {
    font-family: "Open Sans", sans-serif; font-weight: 300;
    font-size: 38px; letter-spacing: 1px; color: var(--brand-dark);
    text-transform: uppercase;
  }

  .letter-body {
    position: absolute; left: 107px; top: 263px; width: 579px;
    font-family: "Open Sans", sans-serif; font-weight: 400;
    font-size: 12.6px; line-height: 18.6px; color: var(--ink);
  }
  .letter-body p { text-align: justify; margin-bottom: 18.6px; }
  .letter-body .salutation { margin-bottom: 18px; text-align: left; }
  .sign-off { position: absolute; left: 107px; top: 764px;
    font-family: "Open Sans", sans-serif; font-size: 12.6px; color: var(--ink); }
  .signature { position: absolute; left: 112px; top: 788px;
    font-family: "Pinyon Script", cursive; font-size: 26px; color: #1d1d1d; }

  .contact-details {
    position: absolute; left: 80px; top: 1037px;
    font-family: "Lora", serif; font-size: 13px; line-height: 17px; color: var(--brand-dark);
  }
  .contact-details div { display: flex; align-items: center; gap: 8px; }
  .contact-details svg { width: 10px; height: 10px; }
  .web-address {
    position: absolute; right: 78px; top: 1054px;
    font-family: "Lora", serif; font-size: 13px; color: var(--brand-dark);
  }
  .accent-bar { position: absolute; right: 78px; top: 1041px; width: 33px; height: 4px; background: var(--accent-orange); }
</style>
</head>
<body>
  <main class="letterhead">
    <div class="color-spine">
      <span class="s1"></span><span class="s2"></span><span class="s3"></span>
      <span class="s4"></span><span class="s5"></span><span class="s6"></span>
    </div>

    <div class="brand-decoration" role="img" aria-label="Faint brand pattern decoration in light grey"></div>

    <header class="brand-lockup">
      <div class="brand-mark"></div>
      <div class="brand-name">Corvale</div>
    </header>

    <section class="letter-body">
      <p class="salutation">Dear Daniel Harwick,</p>
      <p>Lorem ipsum dolor sit amet, consectetuer adipiscing elit, sed diam nonummy nibh euismod tincidunt ut laoreet dolore magna aliquam erat volutpat. Ut wisi enim ad minim veniam, quis nostrud exerci tation ullamcorper suscipit lobortis nisl ut aliquip ex ea commodo consequat. Duis dolore te feugait nulla facilisi. Nam liber tempor cum soluta nobis eleifend option congue nihil imperdiet doming id quod mazim placerat facer possim assum. Lorem ipsum dolor sit amet, consectetuer adipiscing elit, sed diam nonummy nibh euismod tincidunt ut laoreet dolore magna aliquam erat volutpat. Ut wisi enim ad minim veniam, quis nostrud exerci tation ullamcorper suscipit lobortis nisl ut aliquip ex ea commodo consequat.</p>
      <p>Consectetuer adipiscing elit, sed diam nonummy nibh euismod tincidunt ut laoreet dolore magna aliquam erat volutpat. Ut wisi enim ad minim veniam, quis nostrud exerci tation ullamcorper suscipit lobortis nisl ut aliquip ex ea commodo consequat. Consectetuer adipiscing elit, sed diam nonummy nibh euismod tincidunt ut laoreet dolore magna aliquam erat volutpat. Ut wisi enim ad minim veniam, quis nostrud exerci tation ullamcorper suscipit lobortis nisl ut aliquip ex ea commodo consequat.</p>
      <p>Consectetuer adipiscing elit, sed diam nonummy nibh euismod tincidunt ut laoreet dolore magna aliquam erat volutpat. Ut wisi enim ad minim veniam, quis nostrud exerci tation ullamcorper suscipit lobortis nisl ut aliquip ex ea commodo consequat. Consectetuer adipiscing elit, sed diam nonummy nibh euismod tincidunt ut laoreet dolore magna aliquam erat volutpat. Ut wisi enim ad minim veniam, quis nostrud exerci tation ullamcorper suscipit lobortis nisl ut aliquip ex ea commodo consequat.</p>
    </section>

    <div class="sign-off">Sincerely Yours</div>
    <div class="signature">Thomas Ellery</div>

    <footer>
      <div class="contact-details">
        <div>
          <svg viewBox="0 0 10 10" aria-hidden="true"><path d="M2 1 L3.6 1 L4.2 3 L3.2 3.8 Q4.2 5.8 6.2 6.8 L7 5.8 L9 6.4 L9 8 Q9 9 8 9 Q1 8.5 1 2 Q1 1 2 1 Z" fill="var(--accent-orange)"/></svg>
          <span>200.555.0148</span>
        </div>
        <div>
          <svg viewBox="0 0 10 10" aria-hidden="true"><rect x="0.5" y="2" width="9" height="6" fill="var(--accent-orange)"/><path d="M0.5 2 L5 5.5 L9.5 2" stroke="var(--paper)" stroke-width="0.9" fill="none"/></svg>
          <span>info@wearecorvale.com</span>
        </div>
      </div>
      <div class="accent-bar"></div>
      <div class="web-address">www.wearecorvale.com</div>
    </footer>
  </main>
</body>
</html>
```